I need a label design for my up coming wine bottle

The bottle is a standard wine bottle, 720 ML. The label needs to be elegant 1-3 colors preferably with grape vines highlighting my winery name. 5-8 cellars

```html
<!DOCTYPE html>
<html lang="en">
<head>
<meta charset="utf-8">
<title>5-8 Cellars – Estate Cabernet Sauvignon Label</title>
<link rel="stylesheet" href="https://fonts.googleapis.com/css2?family=Bodoni+Moda:wght@500&family=Great+Vibes&display=swap">
<style>
  :root {
    --page: #ffffff;
    --label-top: #2b2b2b;
    --label-mid: #1c1c1c;
    --band: #333333;
    --rule: #6a6a6a;
    --gold: #a88a5a;
    --cream: #f4efe4;
    --scene-light: #353535;
    --scene-dark: #151515;
  }
  html, body {
    margin: 0;
    padding: 0;
    width: 1200px;
    height: 2400px;
    overflow: hidden;
    background: var(--page);
  }
  .canvas {
    position: relative;
    width: 1200px;
    height: 2400px;
  }
  .label {
    position: absolute;
    left: 150px;
    top: 338px;
    width: 900px;
    height: 1724px;
    filter: drop-shadow(0 4px 10px rgba(0,0,0,0.15));
  }
  .label-shape {
    position: absolute;
    inset: 0;
    width: 900px;
    height: 1724px;
  }
  .winery-name,
  .wine-name,
  .varietal,
  .vintage {
    position: absolute;
    left: 0;
    width: 900px;
    margin: 0;
    text-align: center;
    font-weight: 500;
  }
  .winery-name {
    top: 208px;
    font-family: "Bodoni Moda", "Didot", serif;
    font-size: 82px;
    line-height: 1;
    letter-spacing: 8px;
    color: var(--gold);
  }
  .wine-name {
    top: 440px;
    font-family: "Bodoni Moda", "Didot", serif;
    font-size: 112px;
    line-height: 106px;
    color: var(--cream);
  }
  .varietal {
    top: 648px;
    font-family: "Great Vibes", cursive;
    font-weight: 400;
    font-size: 118px;
    line-height: 1;
    color: var(--gold);
  }
  .vintage {
    top: 1300px;
    font-family: "Bodoni Moda", "Didot", serif;
    font-size: 124px;
    line-height: 1;
    color: var(--gold);
  }
</style>
</head>
<body>
<main class="canvas">
  <section class="label">
    <svg class="label-shape" viewBox="0 0 900 1724" xmlns="http://www.w3.org/2000/svg">
      <defs>
        <linearGradient id="label-fill" x1="0" y1="0" x2="0" y2="1">
          <stop offset="0" stop-color="#2b2b2b"/>
          <stop offset="0.45" stop-color="#1c1c1c"/>
        </linearGradient>
        <linearGradient id="vineyard-fill" x1="0" y1="0" x2="0" y2="1">
          <stop offset="0" stop-color="#1c1c1c"/>
          <stop offset="0.35" stop-color="#353535"/>
          <stop offset="1" stop-color="#151515"/>
        </linearGradient>
        <clipPath id="label-clip">
          <path d="M160 0 H740 L900 142 V1299 C900 1550 700 1724 450 1724 C200 1724 0 1550 0 1299 V142 Z"/>
        </clipPath>
      </defs>
      <g clip-path="url(#label-clip)">
        <rect class="label-body" x="0" y="0" width="900" height="1724" fill="url(#label-fill)"/>
        <rect class="vintage-band" x="0" y="1196" width="900" height="528" fill="#333333"/>
        <rect class="vineyard-scene" x="0" y="779" width="900" height="417" fill="url(#vineyard-fill)"
              role="img" aria-label="Engraved vineyard landscape with rows of vines, a farmhouse, wine glasses, a bottle and a barrel"/>
      </g>
      <path class="inner-frame" d="M176 54 H724 L862 176 V1299 C862 1520 680 1686 450 1686 C220 1686 38 1520 38 1299 V176 Z"
            fill="none" stroke="#6a6a6a" stroke-width="5" opacity="0.8"/>
    </svg>

    <h1 class="winery-name">5-8 CELLARS</h1>
    <h2 class="wine-name">ESTATE<br>CABERNET</h2>
    <p class="varietal">Sauvignon</p>
    <p class="vintage">2022</p>
  </section>
</main>
</body>
</html>
```